Lumo's Salon (Business Cards) Needed

I need a new business card for my hair salon based in Fairfax, VA called "Lumo's Salon". I have been in business at the same location for the past 15 years, and have recently remodeled the place to be a little bit more upscale and modern. Previously, my clientele's were mostly men, but now I would like to attract more female clientele into my business. I would like the design to attract the female's attention with it's modern touch, flowery, freshness with just enough information and not too compact. Simple, clean and professional is the look.
Requirements
Must Have:
- The design should include:
Business name: Lumo's Salon
Hairstylist/Owner Name: Dara Pelkin
Phone Number: (555) 481-6037
Website: www.lumohairstudio.example
Address: 48913 Orrin Bellwood Lane
Brookmere, ZX 00000
FRONT CARD should include:
- Logo (Business name)
- Slogan (Your style, our craft)
BACK CARD should include:
- Logo (Business name)
- Hairstyle name
- Phone number
- Website
- Address
Updates
Reason: There were some good submission for this project, but most of the submission were poorly designed, and did not have what I want. There isn't enough designs for me to choose from and not one of it stood out to me. I would like to extend it a bit longer to see if any other designer would step up to the plate, and deliver. Thank you.
Industry/Entity Type
Hair
Requirements
Must have
- The front side of the business card should only have the business name (Lumo's Salon) and slogan, (Your beauty our passion) with a creative design.
The back side of the business card should have all the business information, and creative design that matches with the front, but not identical.
The first letter (V) in (Lumo's) should have a flower design connected to it, which blends into the background design.
Nice to have
- Light color scheme.
Should not have
- The front, and back should not have the same design.
Do not include illustrations of a pair of scissors, combs or any objects in the design.
The design should not take the main focus from the business name and business information. It should blend well together... if that's possible.

```html
<!DOCTYPE html>
<html lang="en">
<head>
<meta charset="utf-8">
<title>Lumo's Salon – Business Cards</title>
<link href="https://fonts.googleapis.com/css2?family=Open+Sans:wght@300;400;600;700&display=swap" rel="stylesheet">
<style>
  :root {
    --canvas-bg: #ececec;
    --front-bg: #d9a4d4;
    --front-band: #8356b6;
    --front-lace: #a575c9;
    --front-logo: #ecd0f1;
    --back-bg: #cfe8e4;
    --back-band: #6fc2dd;
    --ink: #222222;
    --ink-soft: #555555;
    --rule: #9aa9a7;
  }
  * { box-sizing: border-box; margin: 0; padding: 0; }
  html, body {
    width: 1200px; height: 1200px; overflow: hidden;
    background: var(--canvas-bg);
    font-family: "Open Sans", sans-serif;
  }
  .sheet { position: relative; width: 1200px; height: 1200px; }
  .card {
    position: absolute; left: 300px; width: 600px; height: 343px;
    overflow: hidden; box-shadow: 0 6px 18px rgba(0,0,0,.12);
  }

  /* Front */
  .card--front { top: 200px; background: var(--front-bg); }
  .front-lace {
    position: absolute; left: 130px; right: 0; top: 98px; height: 150px;
    background: var(--front-lace);
  }
  .front-band {
    position: absolute; left: 130px; right: 0; top: 118px; height: 110px;
    background: var(--front-band);
  }
  .front-logo {
    position: absolute; left: 160px; top: 128px;
    font-size: 42px; font-weight: 600; color: var(--front-logo);
    white-space: nowrap;
  }
  .front-slogan {
    position: absolute; left: 162px; top: 188px;
    font-size: 17px; font-weight: 300; color: var(--front-logo);
    white-space: nowrap;
  }

  /* Back */
  .card--back { top: 620px; background: var(--back-bg); }
  .back-logo {
    position: absolute; left: 58px; top: 62px;
    font-size: 30px; font-weight: 600; color: var(--ink);
    white-space: nowrap;
  }
  .back-slogan {
    position: absolute; left: 60px; top: 104px;
    font-size: 13px; font-weight: 300; color: var(--ink-soft);
    white-space: nowrap;
  }
  .back-address {
    position: absolute; left: 40px; top: 172px;
    font-size: 14px; line-height: 1.4; color: var(--ink-soft);
    font-style: normal; white-space: nowrap;
  }
  .name-band {
    position: absolute; left: 320px; right: 0; top: 150px; height: 62px;
    background: var(--back-band); padding: 8px 0 0 22px;
  }
  .name-band__name { font-size: 20px; font-weight: 700; color: var(--ink); line-height: 1.2; }
  .name-band__role { font-size: 13px; color: var(--ink); }
  .contact-rule {
    position: absolute; left: 300px; top: 226px; width: 1px; height: 56px;
    background: var(--rule);
  }
  .contact-list {
    position: absolute; left: 312px; top: 228px; list-style: none;
    font-size: 15px; color: var(--ink); line-height: 26px; white-space: nowrap;
  }
  .contact-list li { display: flex; align-items: center; gap: 8px; }
  .contact-list svg { width: 14px; height: 14px; flex: none; }
</style>
</head>
<body>
<main class="sheet">
  <section class="card card--front" aria-label="Front of business card">
    <div class="front-lace" role="img" aria-label="Lace scallop border pattern"></div>
    <div class="front-band"></div>
    <div class="front-logo">Lumo's Salon</div>
    <div class="front-slogan">Your style, our craft</div>
  </section>

  <section class="card card--back" aria-label="Back of business card">
    <div class="back-logo">Lumo's Salon</div>
    <div class="back-slogan">Your style, our craft</div>
    <address class="back-address">
      48913 Orrin Bellwood Lane<br>Brookmere, ZX 00000
    </address>
    <div class="name-band">
      <div class="name-band__name">Dara Pelkin</div>
      <div class="name-band__role">Hairstylist/Owner</div>
    </div>
    <div class="contact-rule"></div>
    <ul class="contact-list">
      <li>
        <svg viewBox="0 0 14 14" aria-hidden="true"><rect width="14" height="14" rx="2" fill="#3a5560"/><path d="M4 3.5c.6 0 1 1.6 1 2 0 .4-.6.6-.4 1 .4.9 1.1 1.6 2 2 .4.2.6-.4 1-.4.4 0 2 .4 2 1 0 .8-.8 1.4-1.6 1.4C5.5 10.5 3.5 8.5 3.5 5.1c0-.8.2-1.6.5-1.6z" fill="#fff"/></svg>
        (555) 481-6037
      </li>
      <li>
        <svg viewBox="0 0 14 14" aria-hidden="true"><circle cx="7" cy="7" r="7" fill="#3a5560"/><circle cx="7" cy="7" r="4.5" fill="none" stroke="#fff" stroke-width="1"/><path d="M2.5 7h9M7 2.5c-2 2.5-2 6.5 0 9M7 2.5c2 2.5 2 6.5 0 9" fill="none" stroke="#fff" stroke-width="0.8"/></svg>
        www.lumohairstudio.example
      </li>
    </ul>
  </section>
</main>
</body>
</html>
```